Business Card Design

We need a business card design for a kids clothes shop in Ireland called "Tiny Trotz". Would prefer the colours Lime Green and Dark Purple to be used but are open to suggestions. The logo should include a "Cool" penguin with clothes on.

Industry/Entity Type

Shop

Contact Information for Business Card

Tiny Trotz
Harlow Arcade,
Ashvale Road, Childrenswear 0-12yrs
Ballyrowan,
XQ82 5LW. Deirdre Walsh.

```html
<!DOCTYPE html>
<html lang="en">
<head>
<meta charset="utf-8">
<title>Tiny Trotz – Business Card</title>
<link rel="stylesheet" href="https://fonts.googleapis.com/css2?family=Kurale&display=swap">
<style>
  :root {
    --teal-core: #22cfa9;
    --teal-mid: #12a88e;
    --teal-edge: #0b7866;
    --panel-light: #a3a3ad;
    --panel-dark: #8a8a94;
    --panel-rim: #c9efe2;
    --ink: #4a1519;
    --mark: #5c5c66;
  }
  * { margin: 0; padding: 0; box-sizing: border-box; }
  html, body {
    width: 1200px;
    height: 750px;
    overflow: hidden;
    background: #ffffff;
  }
  .card {
    position: relative;
    width: 1200px;
    height: 750px;
    overflow: hidden;
    background:
      radial-gradient(ellipse 55% 60% at 62% 45%, var(--teal-core) 0%, rgba(34,207,169,0) 70%),
      repeating-linear-gradient(90deg, rgba(255,255,255,0.035) 0 3px, rgba(0,0,0,0.03) 3px 7px, rgba(255,255,255,0) 7px 12px),
      linear-gradient(180deg, var(--teal-edge) 0%, var(--teal-mid) 30%, var(--teal-mid) 70%, var(--teal-edge) 100%);
    font-family: "Kurale", Georgia, serif;
    color: var(--ink);
  }
  .panel {
    position: absolute;
    background: linear-gradient(180deg, var(--panel-light) 0%, var(--panel-dark) 100%);
    box-shadow: 0 0 0 2px var(--panel-rim), 0 0 10px rgba(200, 255, 235, 0.35);
  }
  .brand-panel {
    left: 0;
    top: 112px;
    width: 697px;
    height: 249px;
  }
  .brand-mark {
    position: absolute;
    left: 90px;
    top: 186px;
    width: 60px;
    height: 60px;
    border-radius: 50%;
    background: var(--mark);
  }
  .brand-name {
    position: absolute;
    left: 187px;
    top: 132px;
    font-size: 70px;
    font-weight: 400;
    line-height: 1;
    letter-spacing: 1px;
    white-space: nowrap;
  }
  .brand-panel .brand-name { top: 78px; }
  .address-panel {
    left: 502px;
    top: 426px;
    width: 698px;
    height: 245px;
    padding: 8px 24px 0 22px;
  }
  .address-heading {
    font-size: 36px;
    font-weight: 400;
    text-align: center;
    line-height: 1.2;
    margin-bottom: 6px;
  }
  .address-lines {
    font-size: 29.5px;
    line-height: 1.5;
    white-space: nowrap;
    font-style: normal;
  }
</style>
</head>
<body>
  <main class="card">
    <section class="panel brand-panel">
      <span class="brand-mark" aria-hidden="true" style="top:96px;"></span>
      <h1 class="brand-name">Tiny Trotz</h1>
    </section>
    <section class="panel address-panel">
      <h2 class="address-heading">Address:</h2>
      <address class="address-lines">
        Tiny Trotz Harlow Arcade, Ashvale Road,<br>
        childrenswear 0-12 yrs Ballyrowan, XQ82 5LW.<br>
        Deirdre Walsh.
      </address>
    </section>
  </main>
</body>
</html>
```